British Columbia Day banner showcasing 20% off site

Banner graphic promoting our BC Day sale
Size: 1800 x 1000
- flag has been uploaded for inspiration
- examples from other companies and their sale banners have been uploaded for inspiration.
- product images can be found at www.kelvoraleaf.com, please use a variety of different products in this banner

Target Market(s)

19+

Industry/Entity Type

Cannabis

Requirements
Must have
• Phrases:
- “Celebrate BC Day with BC bud and companies”
- “20% off site wide sale*"
- Underneath phrase the date of sale “July 30th - August 3rd”
- In tiny print “*excludes all sale and bundled items”
- MUST BE 1800 X1000
Nice to have
• - images of the products or bud we carry which can be found at www.kelvoraleaf.com
- bold
Should not have
• - company logo

```html
<!DOCTYPE html>
<html lang="en">
<head>
<meta charset="utf-8">
<title>BC Day Sale Banner</title>
<link rel="stylesheet" href="https://fonts.googleapis.com/css2?family=Fjalla+One&family=Krona+One&family=Open+Sans:wght@600&display=swap">
<style>
  :root {
    --black: #000000;
    --green: #8dc63f;
    --white: #ffffff;
  }
  html, body {
    margin: 0;
    padding: 0;
    width: 1200px;
    height: 670px;
    overflow: hidden;
    background: var(--black);
  }
  .banner {
    position: relative;
    width: 1200px;
    height: 670px;
    background: var(--black);
    overflow: hidden;
  }
  .headline {
    position: absolute;
    left: 72px;
    top: 110px;
    margin: 0;
    font-family: "Fjalla One", sans-serif;
    font-weight: 400;
    font-size: 62px;
    line-height: 78px;
    color: var(--green);
    letter-spacing: -0.5px;
  }
  .brand {
    position: absolute;
    left: 900px;
    top: 140px;
    width: 240px;
    display: flex;
    align-items: center;
    gap: 14px;
    font-family: "Krona One", sans-serif;
    font-size: 24px;
    color: var(--white);
    white-space: nowrap;
  }
  .brand-square {
    width: 30px;
    height: 30px;
    background: var(--green);
    flex: none;
  }
  .offer-band {
    position: absolute;
    left: 0;
    top: 340px;
    width: 1200px;
    height: 275px;
    background: var(--green);
  }
  .offer {
    position: absolute;
    left: 90px;
    top: 38px;
    margin: 0;
    display: flex;
    align-items: baseline;
    white-space: nowrap;
    color: var(--black);
    font-family: "Krona One", sans-serif;
  }
  .offer-percent {
    font-size: 108px;
    letter-spacing: -2px;
    margin-right: 46px;
  }
  .offer-text {
    font-size: 42px;
    letter-spacing: 1px;
  }
  .dates {
    position: absolute;
    left: 0;
    top: 188px;
    width: 100%;
    margin: 0;
    text-align: center;
    font-family: "Krona One", sans-serif;
    font-size: 30px;
    color: var(--white);
    letter-spacing: 1px;
  }
  .fine-print {
    position: absolute;
    left: 0;
    top: 615px;
    width: 100%;
    height: 55px;
    margin: 0;
    display: flex;
    align-items: center;
    justify-content: center;
    font-family: "Open Sans", sans-serif;
    font-weight: 600;
    font-size: 18px;
    letter-spacing: 2.5px;
    color: var(--green);
  }
</style>
</head>
<body>
  <main class="banner">
    <h1 class="headline">Celebrate BC Day with<br>BC bud and companies</h1>

    <div class="brand">
      <span class="brand-square"></span>
      <span class="brand-name">Kelvora Leaf</span>
    </div>

    <section class="offer-band">
      <p class="offer">
        <span class="offer-percent">20%</span>
        <span class="offer-text">off site wide sale*</span>
      </p>
      <p class="dates">July 30th - August 3rd</p>
    </section>

    <p class="fine-print">*excludes all sale and bundled items</p>
  </main>
</body>
</html>
```